Copper Lark Treks Flyer

I have an adventure travel company and I need a flyer to promote my trip to Ukraine.
I would like to have a universal flyer that I can change based on the trip.
The Title should say "Travel to Ukraine: 9 Day Eastern European Adventure"
The date should be under the title.
The background photo should be kiev2.jpg
The highlights of the trip, then price $1200 and what it includes. See the text for highlights and includes sections here:
http://www.copperlarktreks.com/#!featured-trip
The website link (www.copperlarktreks.com) should be somewhere in the bottom.
You can use other photos provided or from my website that relates to Ukraine trip.

```html
<!DOCTYPE html>
<html lang="en">
<head>
<meta charset="utf-8">
<title>Copper Lark Treks – Travel to Ukraine</title>
<link href="https://fonts.googleapis.com/css2?family=Arvo:ital,wght@0,700;1,700&family=PT+Sans+Narrow:wght@400;700&family=PT+Sans:wght@700&display=swap" rel="stylesheet">
<style>
  :root {
    --sky: #7fd0f2;
    --sky-deep: #1e9ad6;
    --title-yellow: #ffe600;
    --accent-yellow: #ffd400;
    --flag-red: #d42a2a;
    --band-red: #cf2027;
    --stripe-blue: #8fd3f0;
    --white: #ffffff;
    --ink: #1a1a1a;
    --footer-red: #c8102e;
  }
  * { margin: 0; padding: 0; box-sizing: border-box; }
  html, body { width: 927px; height: 1200px; overflow: hidden; background: var(--white); }
  .flyer { position: relative; width: 927px; height: 1200px; overflow: hidden; background: var(--white); }

  .hero-photo {
    position: absolute; left: 0; top: 110px; width: 927px; height: 600px;
    background:
      radial-gradient(ellipse at 55% 55%, #e4b43a 0%, #b98a2a 18%, rgba(120,110,90,0) 40%),
      linear-gradient(180deg, #6f8f9c 0%, #56705a 25%, #4f6a45 50%, #6b6a5c 75%, #7a7466 100%);
  }

  .header-wave { position: absolute; left: 0; top: 0; width: 927px; height: 200px; }

  .title {
    position: absolute; left: 0; top: 14px; width: 927px; text-align: center;
    font-family: "Arvo", Georgia, serif; font-weight: 700; font-style: italic;
    font-size: 47px; line-height: 52px; color: var(--title-yellow);
    text-shadow: 2px 2px 0 #1b6fa8;
  }
  .dates {
    position: absolute; left: 0; top: 120px; width: 927px; text-align: center;
    font-family: "PT Sans", Arial, sans-serif; font-weight: 700; font-size: 30px;
    color: var(--white);
  }

  .snapshot {
    position: absolute; border: 5px solid var(--white);
    box-shadow: 2px 3px 6px rgba(0,0,0,0.5);
  }
  .snapshot--cave { left: 38px; top: 112px; width: 205px; height: 165px; transform: rotate(10deg);
    background: radial-gradient(circle at 45% 50%, #e2b27a, #9a5a2c 60%, #4a2414); }
  .snapshot--cathedral { left: 665px; top: 142px; width: 235px; height: 170px; transform: rotate(-8deg);
    background: linear-gradient(180deg, #c9d7e8 0%, #e8e2c8 45%, #c8b070 60%, #6d8a52 100%); }
  .snapshot--coast { left: 44px; top: 616px; width: 229px; height: 147px;
    background: linear-gradient(180deg, #9fc2e0 0%, #3f7ba8 40%, #3f7540 60%, #2f5a2c 100%); }
  .snapshot--tram { left: 354px; top: 616px; width: 229px; height: 147px;
    background: linear-gradient(180deg, #a8b5b8 0%, #7d8a74 45%, #9a4b3e 62%, #777 100%); }
  .snapshot--mountain { left: 685px; top: 616px; width: 198px; height: 147px;
    background: linear-gradient(180deg, #7f9fbf 0%, #b0bccb 45%, #8b8a80 70%, #5c5e4c 100%); }

  .stripe { position: absolute; left: 0; width: 927px; }
  .stripe--light { top: 700px; height: 9px; background: var(--stripe-blue); }

  .info-band { position: absolute; left: 0; top: 709px; width: 927px; height: 420px; background: var(--band-red); }

  .section-heading {
    position: absolute; left: 62px;
    font-family: "Arvo", Georgia, serif; font-weight: 700; font-size: 22px;
    color: var(--accent-yellow); letter-spacing: 0.5px;
  }
  .section-heading--highlights { top: 773px; }
  .section-heading--included { top: 968px; }

  .highlights { position: absolute; left: 50px; top: 810px; list-style: none; }
  .highlights li {
    position: relative; padding-left: 20px; height: 26.6px;
    font-family: "PT Sans Narrow", Arial Narrow, sans-serif; font-size: 17.2px; line-height: 26.6px;
    color: var(--white); white-space: nowrap;
  }
  .highlights li svg { position: absolute; left: 0; top: 8px; width: 15px; height: 12px; }
  .hl { color: var(--accent-yellow); }

  .included { position: absolute; left: 56px; top: 1001px; list-style: none; }
  .included li {
    height: 26px; font-family: "PT Sans Narrow", Arial Narrow, sans-serif; font-size: 17.2px; line-height: 26px;
    color: var(--white); white-space: nowrap;
  }
  .included li::before { content: "•"; margin-right: 7px; }

  .price-badge {
    position: absolute; left: 780px; top: 792px; width: 120px; height: 120px; border-radius: 50%;
    background: var(--title-yellow); border: 3px solid #e23a2a;
    display: flex; flex-direction: column; align-items: center; justify-content: center;
    font-family: "Arvo", Georgia, serif; font-weight: 700; color: var(--band-red);
    transform: rotate(-12deg);
  }
  .price-badge__label { font-size: 19px; line-height: 22px; }
  .price-badge__amount { font-size: 27px; line-height: 30px; }

  .footer { position: absolute; left: 0; top: 1129px; width: 927px; height: 71px; background: var(--white); }
  .contact {
    position: absolute; top: 3px; text-align: center;
    font-family: "PT Sans Narrow", Arial Narrow, sans-serif; font-weight: 700; font-size: 13px; line-height: 16px;
    color: var(--ink);
  }
  .contact--left { left: 12px; width: 220px; }
  .contact--right { right: 12px; width: 220px; text-align: right; }
  .contact__name { color: var(--footer-red); }
  .contact--right .contact__name { text-align: center; display: block; padding-left: 40px; }
  .contact a { color: var(--footer-red); text-decoration: none; }
  .site-url {
    position: absolute; left: 0; top: 1163px; width: 927px; text-align: center;
    font-family: "Arvo", Georgia, serif; font-weight: 700; font-size: 26px; color: var(--footer-red);
  }
</style>
</head>
<body>
<div class="flyer">
  <div class="hero-photo" role="img" aria-label="Aerial view of a Kiev monastery with golden onion domes above the Dnieper river"></div>

  <svg class="header-wave" viewBox="0 0 927 200" aria-hidden="true">
    <defs>
      <linearGradient id="skyFill" x1="0" y1="0" x2="0" y2="1">
        <stop offset="0" stop-color="#ffffff"/>
        <stop offset="0.35" stop-color="#bfe7f8"/>
        <stop offset="1" stop-color="#4fb6e6"/>
      </linearGradient>
    </defs>
    <path d="M0 0 H927 V150 Q700 205 463 185 Q220 165 0 130 Z" fill="url(#skyFill)"/>
    <path d="M0 130 Q220 165 463 185 Q700 205 927 150 V160 Q700 215 463 195 Q220 175 0 140 Z" fill="#1e9ad6"/>
  </svg>

  <h1 class="title">"Travel to Ukraine: 9 Day Eastern<br>European Adventure"</h1>
  <p class="dates">Fri May 18 -&nbsp; Sun May 27</p>

  <div class="snapshot snapshot--cave" role="img" aria-label="Stalactite formations inside a Crimean cave"></div>
  <div class="snapshot snapshot--cathedral" role="img" aria-label="White cathedral with golden domes in Kiev"></div>

  <div class="stripe stripe--light"></div>
  <div class="info-band"></div>

  <div class="snapshot snapshot--coast" role="img" aria-label="Green Crimean coastline above the Black Sea"></div>
  <div class="snapshot snapshot--tram" role="img" aria-label="Red tram on an old tree-lined city street"></div>
  <div class="snapshot snapshot--mountain" role="img" aria-label="Pine tree on a rocky Crimean mountain"></div>

  <h2 class="section-heading section-heading--highlights">HIGHLIGHTS:</h2>
  <ul class="highlights">
    <li><svg viewBox="0 0 15 12"><path d="M1 6 L5.5 10.5 L14 1" fill="none" stroke="#ffd400" stroke-width="2.4"/></svg>Discover <span class="hl">Kiev</span>- the birthplace of Eastern Slavic Civilization</li>
    <li><svg viewBox="0 0 15 12"><path d="M1 6 L5.5 10.5 L14 1" fill="none" stroke="#ffd400" stroke-width="2.4"/></svg>Meet <span class="hl">Crimea's</span> fascinating <span class="hl">Tatar</span> Minority in Bakhchysaray - former capital of Crimean Tatar Khans</li>
    <li><svg viewBox="0 0 15 12"><path d="M1 6 L5.5 10.5 L14 1" fill="none" stroke="#ffd400" stroke-width="2.4"/></svg>Walk to <span class="hl">Chufut-Kale</span> - Crimea's best preserved&nbsp; medieval cave town</li>
    <li><svg viewBox="0 0 15 12"><path d="M1 6 L5.5 10.5 L14 1" fill="none" stroke="#ffd400" stroke-width="2.4"/></svg><span class="hl">Hike</span> in the most spectacular areas in Karabi and&nbsp;&nbsp; with a group of professional speleologist</li>
    <li><svg viewBox="0 0 15 12"><path d="M1 6 L5.5 10.5 L14 1" fill="none" stroke="#ffd400" stroke-width="2.4"/></svg>Inhale the magic <span class="hl">Yalta's air</span>- an invigorating blend of sea and pine forest sprinkled with mountain chill</li>
    <li><svg viewBox="0 0 15 12"><path d="M1 6 L5.5 10.5 L14 1" fill="none" stroke="#ffd400" stroke-width="2.4"/></svg>Visit <span class="hl">Odessa</span>- "the Pearl by the Black Sea", Catacombs, Opera house, the factory of sparkling wines and famous <span class="hl">Potemkin Steps</span></li>
  </ul>

  <div class="price-badge">
    <span class="price-badge__label">PRICE</span>
    <span class="price-badge__amount">$1200</span>
  </div>

  <h2 class="section-heading section-heading--included">INCLUDED:</h2>
  <ul class="included">
    <li>9 nights accommodations</li>
    <li>Breakfast, lunch and dinner daily</li>
    <li>English speaking tour guides and transportation at every destination.</li>
    <li>Tour leader from USA at all times during the trip.</li>
    <li>All Group Transfers (trains, buses and vans),&nbsp; sightseeing tours and entrance fees</li>
  </ul>

  <footer class="footer">
    <div class="contact contact--left">
      <span class="contact__name">Olena Marchuk</span><br>
      Main +1.555.014.2200<br>
      Fax&nbsp; +1.555.019.4410<br>
      Email <a href="mailto:olena@copperlarktreks.com">olena@copperlarktreks.com</a>
    </div>
    <div class="contact contact--right">
      <span class="contact__name">Deniz Aral</span>
      Main +1.555.016.7300<br>
      Fax&nbsp; +1.555.019.4410<br>
      Email <a href="mailto:deniz@copperlarktreks.com">deniz@copperlarktreks.com</a>
    </div>
  </footer>
  <p class="site-url">www.copperlarktreks.com</p>
</div>
</body>
</html>
```